Copper Hollow Sparkling

Hi all,

Thanks for taking the time to check out our brief.

Copper Hollow is an Australian wine company based in Victoria, and have been around for more than 20 years. We have a well-known sparkling Chardonnay Pinot Noir that needs a package revamp and we need your help!

Check out our current package here: http://www.copperhollowvino.com.au/our-wines/dsp-default_b.cfm?loadref=17

So here's the brief:

1. Use of the Copper Hollow logo (silhouette) and text mandatory - but can be as small/large as required.

2. Design must be shown on a sparkling bottle.

3. Can be closed with cork or crown seal - neck label/hood not mandatory.

4. Front label size to be no larger than 75mm high x 100mm wide. Back label to be no larger than 75mm x 100mm

5. Label does not have to be square/rectangular. Happy to see thoughts outside the box.

6. Design cannot be printed onto the bottle - must be on a label that can be applied to the bottle.

7. Be forward thinking. Be interesting. This design does not have to tie into our still (red and white) wine range.

8. Mandatory information to be shown on front label - a. Wine of Australia - b. Sparkling Chardonnay Pinot Noir

9. Mandatory info for front label - a. 750mL - b. Alcohol e.g. 13.5% ALC/VOL - c. Wine of Australi - d. Producer address (please insert dummy address at this stage - e. standard drinks e.g. approx 8.0 standard drinks (this can also be shown in the standard drinks glass logo) - f. space for a tasting blurb

10. Try to stay away from anything floral or overly girly.

Industry/Entity Type

Floral

Requirements
Must have
• Design must be shown on a sparkling wine bottle & include the full label design separately
Should not have
• Try to stay away from anything too floral and overly girly.

```html
<!DOCTYPE html>
<html lang="en">
<head>
<meta charset="utf-8">
<title>Copper Hollow Sparkling – Front Label</title>
<link href="https://fonts.googleapis.com/css2?family=Marcellus&family=Varela+Round&family=Arimo&display=swap" rel="stylesheet">
<style>
  :root {
    --page: #e4e4e4;
    --copper-light: #e2ab8b;
    --copper-mid: #cf8d66;
    --copper-deep: #b86a42;
    --wine-red: #a3222c;
    --cream: #ecebc6;
    --ink: #141414;
    --ink-soft: #2a2a2a;
  }
  * { margin: 0; padding: 0; box-sizing: border-box; }
  html, body {
    width: 900px;
    height: 1200px;
    overflow: hidden;
    background: var(--page);
  }
  .canvas {
    position: relative;
    width: 900px;
    height: 1200px;
  }
  .label {
    position: absolute;
    left: 40px;
    top: 150px;
    width: 820px;
    height: 900px;
  }
  .label-shape {
    position: absolute;
    inset: 0;
    width: 100%;
    height: 100%;
  }
  .brand-mark {
    position: absolute;
    left: 320px;
    top: 110px;
    width: 470px;
    height: 300px;
    display: flex;
    align-items: center;
    justify-content: center;
    gap: 22px;
  }
  .brand-mark__dot {
    width: 46px;
    height: 46px;
    border-radius: 50%;
    background: var(--cream);
  }
  .brand-mark__name {
    font-family: "Marcellus", serif;
    font-size: 54px;
    color: var(--cream);
    line-height: 1.05;
  }
  .wine-name {
    position: absolute;
    left: 18px;
    top: 530px;
    width: 800px;
    font-family: "Marcellus", serif;
    font-size: 50px;
    letter-spacing: 0.28em;
    color: var(--ink);
    white-space: nowrap;
  }
  .wine-style {
    position: absolute;
    left: 18px;
    top: 596px;
    font-family: "Varela Round", sans-serif;
    font-size: 33px;
    letter-spacing: 0.02em;
    color: var(--ink-soft);
    white-space: nowrap;
  }
  .wine-style::before {
    content: "";
    position: absolute;
    left: 0;
    top: -6px;
    width: 790px;
    height: 2px;
    background: var(--ink-soft);
  }
  .label-facts {
    position: absolute;
    left: 60px;
    top: 770px;
    list-style: none;
    font-family: "Arimo", sans-serif;
    font-size: 31px;
    line-height: 1.3;
    color: var(--ink);
  }
</style>
</head>
<body>
<main class="canvas">
  <section class="label">
    <svg class="label-shape" viewBox="0 0 820 900" aria-hidden="true">
      <defs>
        <linearGradient id="copper" x1="0" y1="0" x2="1" y2="1">
          <stop offset="0" stop-color="var(--copper-light)"/>
          <stop offset="0.5" stop-color="var(--copper-mid)"/>
          <stop offset="1" stop-color="var(--copper-light)"/>
        </linearGradient>
      </defs>
      <path class="label-accent" fill="var(--wine-red)"
            d="M380 40 Q520 0 720 30 Q800 40 810 120 L810 840 Q790 880 720 880 L380 880 Z"/>
      <rect class="label-body" x="0" y="60" width="800" height="840" rx="70" ry="70" fill="url(#copper)"/>
    </svg>

    <div class="brand-mark">
      <span class="brand-mark__dot"></span>
      <span class="brand-mark__name">Copper Hollow</span>
    </div>

    <h1 class="wine-name">COPPER HOLLOW</h1>
    <p class="wine-style">Sparkling Chardonnay Pinot Noir</p>

    <ul class="label-facts">
      <li>Wine of Australia</li>
      <li>13.5% ALC/VOL</li>
      <li>750ml</li>
    </ul>
  </section>
</main>
</body>
</html>
```